New Zealand Export company needs business cards

We need new business cards to match our new logo for a company based in New Zealand who deal specifically with the Pacific Islands. We source, consolidate and ship products out of New Zealand to the Pacific Islands. Will attach our old ones and also new logo.
Would like the Islands we deal with and the areas of work we have access to, to be included on the business cards.

Contact Information for Business Card

T +64 9 571 3048
F +64 9 571 6285
12-18 Kowhai Lane, Drury, 2113
PO Box 814, Drury, Auckland 2247, New Zealand
www.falconfreight.example.nz
E sales@falconfreight.example.nz

Font styles to use
Sans Serif

Colors
85abd2
33a6d7
ffffff

Requirements
Must have
• A company of PWM

```html
<!DOCTYPE html>
<html lang="en">
<head>
<meta charset="utf-8">
<title>Falcon Freight – Business Card</title>
<link rel="stylesheet" href="https://fonts.googleapis.com/css2?family=Lato:wght@400;700&display=swap">
<style>
  :root {
    --backdrop: #e1e1e1;
    --card-white: #ffffff;
    --brand-blue: #0b57a2;
    --brand-sky: #3fbbe8;
    --ink: #222222;
    --rule: #8a8a8a;
  }
  * { margin: 0; padding: 0; box-sizing: border-box; }
  html, body { width: 1200px; height: 1200px; overflow: hidden; }
  body {
    background: var(--backdrop);
    font-family: "Lato", sans-serif;
    position: relative;
  }
  .card {
    position: absolute;
    left: 180px;
    width: 840px;
    height: 480px;
    border-radius: 20px;
    box-shadow: 3px 4px 6px rgba(0,0,0,0.28);
  }
  .card--front { top: 80px; background: var(--card-white); }
  .card--back { top: 640px; background: var(--brand-blue); }

  .brand {
    position: absolute;
    display: flex;
    align-items: center;
    gap: 16px;
    font-weight: 700;
    letter-spacing: 1px;
    white-space: nowrap;
  }
  .brand__square { width: 28px; height: 28px; flex: none; }
  .card--front .brand {
    left: 74px; top: 172px;
    font-size: 34px; color: var(--brand-blue);
  }
  .card--front .brand__square { background: var(--brand-blue); }

  .divider {
    position: absolute;
    left: 420px; top: 132px;
    width: 2px; height: 220px;
    background: linear-gradient(to bottom, transparent, var(--rule) 15%, var(--rule) 85%, transparent);
  }
  .contact {
    position: absolute;
    left: 445px; top: 120px;
    color: var(--ink);
  }
  .contact__name {
    font-size: 27px; font-weight: 700; color: var(--brand-blue);
    line-height: 1.1;
  }
  .contact__role { font-size: 19px; line-height: 1.2; }
  .contact__address { margin-top: 14px; font-size: 19px; line-height: 24px; }
  .contact__list { list-style: none; margin-top: 14px; font-size: 19px; }
  .contact__list li { display: flex; align-items: center; gap: 12px; height: 28px; }
  .contact__list li + li { margin-top: 2px; }
  .contact__list svg { width: 18px; height: 18px; fill: var(--brand-blue); flex: none; }

  .card--back .brand {
    left: 0; right: 0; top: 196px;
    justify-content: center;
    font-size: 48px; color: var(--card-white);
  }
  .card--back .brand__square { background: var(--card-white); width: 40px; height: 40px; }
  .website {
    position: absolute;
    left: 0; right: 0; top: 422px;
    text-align: center;
    color: var(--card-white);
    font-size: 19px;
  }
</style>
</head>
<body>
  <section class="card card--front">
    <div class="brand"><span class="brand__square"></span>FALCON FREIGHT</div>
    <div class="divider"></div>
    <div class="contact">
      <p class="contact__name">MARA TANE</p>
      <p class="contact__role">CEO</p>
      <p class="contact__address">12-18 Kowhai Lane, Drury, 2113<br>PO Box 814, Drury, Auckland 2247<br>New Zealand</p>
      <ul class="contact__list">
        <li>
          <svg viewBox="0 0 24 24" aria-hidden="true"><path d="M6.6 10.8a15.1 15.1 0 0 0 6.6 6.6l2.2-2.2a1 1 0 0 1 1-.25 11.4 11.4 0 0 0 3.6.57 1 1 0 0 1 1 1V20a1 1 0 0 1-1 1A17 17 0 0 1 3 4a1 1 0 0 1 1-1h3.5a1 1 0 0 1 1 1c0 1.25.2 2.45.57 3.57a1 1 0 0 1-.25 1z"/></svg>
          +64 9 571 3048
        </li>
        <li>
          <svg viewBox="0 0 24 24" aria-hidden="true"><path d="M7 2h10a2 2 0 0 1 2 2v16a2 2 0 0 1-2 2H7a2 2 0 0 1-2-2V4a2 2 0 0 1 2-2zm0 3v12h10V5zm5 13.5a1 1 0 1 0 0 2 1 1 0 0 0 0-2z"/></svg>
          +64 9 571 6285
        </li>
        <li>
          <svg viewBox="0 0 24 24" aria-hidden="true"><path d="M2 5h20v14H2zm2 2v.4l8 5.6 8-5.6V7zm0 2.8V17h16V9.8l-8 5.6z"/></svg>
          sales@falconfreight.example.nz
        </li>
      </ul>
    </div>
  </section>

  <section class="card card--back">
    <div class="brand"><span class="brand__square"></span>FALCON FREIGHT</div>
    <p class="website">www.falconfreight.example.nz</p>
  </section>
</body>
</html>
```